Artwork flyer ( named LO MI RA ) for my music festival

I need a flyer artwork created for my indie pop, rock, hip-hop and dance music festival as soon as possible. The festival is for ages 18 to 30. Need flyer to be able to be abstracted so i can export into different social media
sizes etc

Here is some information around the music festival details.

Title: LO MI RA ( music festival)

Artists :
PELI Fold
Moira Flint
KRTs
The Brellows
Zint Vobs
Tidal Baron
Velvet no
Amber Frost

Venue: Harrowby Paddock Club
Date: Saturday 25th March
Tickets: www.gatelyne.com.au

Logo Text

LOMI RA ( or LO MI RA)

```html
<!DOCTYPE html>
<html lang="en">
<head>
<meta charset="utf-8">
<title>LO MI RA Music Festival Flyer</title>
<link rel="stylesheet" href="https://fonts.googleapis.com/css2?family=Oswald:wght@500&family=Poppins:wght@700;800&display=swap">
<style>
  :root {
    --page: #ffffff;
    --ink-deep: #1d0c48;
    --ink-mid: #3a1674;
    --white: #ffffff;
    --cyan: #16f1f5;
    --magenta: #c20bcc;
    --teal: #12b59a;
    --teal-blue: #1a86b8;
    --accent-circle: #2a1a8c;
  }
  html, body {
    margin: 0;
    padding: 0;
    width: 1200px;
    height: 2340px;
    overflow: hidden;
    background: var(--page);
  }
  .flyer {
    position: absolute;
    left: 50px;
    top: 459px;
    width: 1057px;
    height: 1367px;
    transform: scale(1.04);
    transform-origin: top left;
    overflow: hidden;
    background: linear-gradient(170deg, var(--ink-mid) 0%, #2a1060 40%, var(--ink-deep) 100%);
    box-shadow: 0 20px 60px rgba(0,0,0,0.35);
    font-family: "Poppins", sans-serif;
    color: var(--white);
  }
  .flyer__art {
    position: absolute;
    inset: 0;
    width: 1057px;
    height: 1367px;
  }
  .flyer__corner {
    position: absolute;
    left: -60px;
    bottom: -60px;
    width: 175px;
    height: 175px;
    border-radius: 50%;
    background: var(--accent-circle);
  }
  .festival-name {
    position: absolute;
    left: 64px;
    top: 92px;
    margin: 0;
    font-weight: 800;
    font-size: 150px;
    line-height: 1;
    letter-spacing: -4px;
    word-spacing: 10px;
    color: var(--white);
    white-space: nowrap;
  }
  .festival-tag {
    position: absolute;
    left: 54px;
    top: 285px;
    width: 683px;
    height: 68px;
    background: var(--magenta);
    display: flex;
    align-items: center;
    justify-content: center;
    font-weight: 800;
    font-size: 50px;
    letter-spacing: 17px;
    padding-left: 17px;
    box-sizing: border-box;
  }
  .event-date {
    position: absolute;
    left: 49px;
    top: 392px;
    width: 600px;
    height: 145px;
  }
  .event-date__day {
    position: absolute;
    left: 0;
    top: -14px;
    font-family: "Oswald", sans-serif;
    font-weight: 500;
    font-size: 150px;
    line-height: 1;
    letter-spacing: -4px;
  }
  .event-date__suffix {
    position: absolute;
    left: 136px;
    top: 2px;
    font-family: "Oswald", sans-serif;
    font-weight: 500;
    font-size: 32px;
    line-height: 1;
  }
  .event-date__month {
    position: absolute;
    left: 175px;
    top: -14px;
    font-weight: 800;
    font-size: 92px;
    line-height: 1;
    color: var(--cyan);
    letter-spacing: -1px;
  }
  .event-date__weekday {
    position: absolute;
    left: 140px;
    top: 66px;
    font-weight: 800;
    font-size: 76px;
    line-height: 1;
    color: var(--magenta);
  }
  .event-date__year {
    position: absolute;
    left: 562px;
    top: 1px;
    width: 36px;
    height: 142px;
    border-radius: 10px;
    background: var(--white);
    color: var(--magenta);
    font-weight: 800;
    font-size: 26px;
    line-height: 33px;
    text-align: center;
    padding-top: 3px;
    box-sizing: border-box;
  }
  .venue {
    position: absolute;
    left: 53px;
    top: 548px;
    margin: 0;
    font-weight: 800;
    font-size: 50px;
    color: var(--cyan);
    white-space: nowrap;
    letter-spacing: -0.5px;
  }
  .lineup__title {
    position: absolute;
    left: 56px;
    top: 643px;
    margin: 0;
    font-weight: 700;
    font-size: 40px;
    color: var(--magenta);
  }
  .lineup__list {
    position: absolute;
    left: 56px;
    top: 720px;
    margin: 0;
    padding: 0;
    list-style: none;
  }
  .lineup__item {
    position: relative;
    padding-left: 33px;
    height: 54px;
    font-weight: 800;
    font-size: 30px;
    line-height: 44px;
    text-transform: uppercase;
  }
  .lineup__item::before {
    content: "";
    position: absolute;
    left: 1px;
    top: 18px;
    width: 8px;
    height: 8px;
    border-radius: 50%;
    background: var(--cyan);
  }
  .tickets__label {
    position: absolute;
    left: 54px;
    top: 1187px;
    margin: 0;
    font-weight: 800;
    font-size: 31px;
    color: var(--cyan);
  }
  .tickets__url {
    position: absolute;
    left: 52px;
    top: 1240px;
    margin: 0;
    font-weight: 800;
    font-size: 30px;
  }
</style>
</head>
<body>
  <main class="flyer">
    <svg class="flyer__art" viewBox="0 0 1057 1367" role="img" aria-label="Illustration of a head in profile with flowing hair full of music notes">
      <defs>
        <linearGradient id="hairGradient" x1="0" y1="0" x2="0" y2="1">
          <stop offset="0" stop-color="#12b59a"/>
          <stop offset="0.45" stop-color="#1a86b8"/>
          <stop offset="0.62" stop-color="#c20bcc"/>
          <stop offset="1" stop-color="#c20bcc"/>
        </linearGradient>
      </defs>
      <path d="M600 0 H1057 V1367 H560 C480 1230 420 1060 520 880 C600 730 700 640 720 470 C740 300 720 110 600 0 Z" fill="url(#hairGradient)"/>
    </svg>
    <div class="flyer__corner"></div>

    <h1 class="festival-name">LO MI RA</h1>
    <div class="festival-tag">MUSIC FESTIVAL</div>

    <div class="event-date">
      <span class="event-date__day">25</span>
      <span class="event-date__suffix">TH</span>
      <span class="event-date__month">MARCH</span>
      <span class="event-date__weekday">SATURDAY</span>
      <span class="event-date__year">2<br>0<br>2<br>3</span>
    </div>

    <p class="venue">HARROWBY PADDOCK CLUB</p>

    <section class="lineup">
      <h2 class="lineup__title">ARTISTS :</h2>
      <ul class="lineup__list">
        <li class="lineup__item">PELI Fold</li>
        <li class="lineup__item">KRTs</li>
        <li class="lineup__item">Zint Vobs</li>
        <li class="lineup__item">Velvet no</li>
        <li class="lineup__item">Moira Flint</li>
        <li class="lineup__item">The Brellows</li>
        <li class="lineup__item">Tidal Baron</li>
        <li class="lineup__item">Amber Frost</li>
      </ul>
    </section>

    <p class="tickets__label">TICKET</p>
    <p class="tickets__url">WWW.GATELYNE.COM.AU</p>
  </main>
</body>
</html>
```